ebook cover for book three in a spiritual iconic series: bold, simple, easy to manage!

The Hollow is the third in a series of memoirs about one woman's spiritual journey over ten years. A PhD, the woman wants to appeal to a broad market and an intellectual market as well as the women's market that makes the core audience. Any Old Kettle is the second book and its cover is currently also commissioned here on Pixel Market if you want to search it. We Grow Radish was the first and its cover is attached for your reference. Please keep the same: the white background, the shade of red for the title, the font for the subtitle and colour, but change the title font and how you use the colour scheme. We look for a slightly enigmatic and also strikingly simple image. The tin can in We Grow Radish is where to start. For Any Old Kettle we have asked for a single Wordlark tablet, the X. Here, we are thinking of the winking smiley attached, but the image needs some photoshopping to make the face a bit more to yellow cold, remove the red ring and so on. The colours to pick from are greys, purple, red, orange, yellow, as with the colors in the flash of light on the tin can in Grow Radish. The idea there was to capture an explosion to new ideas while referencing a key scene involving cooking with tomatoes!

The Hollow

Book details:
Title: The Hollow
Subtitle: Brother Osric presents Veldora
Image ideas: Winking smiley attached, princess castle in the right colours, magic wand.
Author: Marla Quince, Ph.D
Strap quote: "Marla Quince is phenomenal in the true sense of the word. Phenomenons occur around her," Paula Drent, Teacher and spiritual healer

```html
<!DOCTYPE html>
<html lang="en">
<head>
<meta charset="utf-8">
<title>The Hollow — Marla Quince Ph.D.</title>
<link rel="stylesheet" href="https://fonts.googleapis.com/css2?family=Cormorant+Garamond:wght@600;700&family=Open+Sans:ital,wght@0,300;0,400;0,600;1,400&display=swap">
<style>
  :root {
    --page-bg: #e4e7e8;
    --cover-bg: #f4f4f4;
    --title-red: #b3121c;
    --ink: #1e1e1e;
    --author-grey: #4f4f4f;
    --smiley-yellow: #f7c600;
    --smiley-deep: #e6a800;
    --wand-black: #161616;
    --shadow: rgba(0, 0, 0, 0.18);
  }
  * { margin: 0; padding: 0; box-sizing: border-box; }
  html, body {
    width: 1200px;
    height: 988px;
    overflow: hidden;
    background: var(--page-bg);
  }
  .cover {
    position: absolute;
    left: 290px;
    top: 24px;
    width: 620px;
    height: 940px;
    background: var(--cover-bg);
    box-shadow: 0 6px 24px var(--shadow);
    text-align: center;
  }
  .strap-quote {
    position: absolute;
    top: 12px;
    left: 44px;
    right: 44px;
    font-family: "Open Sans", sans-serif;
    font-weight: 600;
    font-size: 11px;
    line-height: 1.6;
    color: var(--ink);
    text-transform: uppercase;
  }
  .strap-quote .attribution {
    font-style: italic;
    font-weight: 400;
  }
  .title {
    position: absolute;
    top: 100px;
    left: 0;
    right: 0;
    font-family: "Cormorant Garamond", serif;
    font-weight: 700;
    font-size: 84px;
    line-height: 1;
    letter-spacing: 0.005em;
    color: var(--title-red);
    white-space: nowrap;
  }
  .subtitle {
    position: absolute;
    top: 258px;
    left: 0;
    right: 0;
    font-family: "Open Sans", sans-serif;
    font-weight: 400;
    font-size: 27px;
    line-height: 1.45;
    letter-spacing: 0.2em;
    color: var(--ink);
    text-transform: uppercase;
  }
  .emblem {
    position: absolute;
    left: 202px;
    top: 440px;
    width: 303px;
    height: 303px;
    border-radius: 50%;
    background: radial-gradient(circle at 40% 36%, var(--smiley-yellow) 58%, var(--smiley-deep) 100%);
  }
  .emblem-shadow {
    position: absolute;
    left: 180px;
    top: 806px;
    width: 340px;
    height: 22px;
    border-radius: 50%;
    background: radial-gradient(ellipse at center, rgba(0,0,0,0.22) 0%, rgba(0,0,0,0) 70%);
  }
  .author {
    position: absolute;
    top: 858px;
    left: 0;
    right: 0;
    font-family: "Open Sans", sans-serif;
    font-weight: 400;
    font-size: 36px;
    letter-spacing: 0.04em;
    color: var(--author-grey);
    text-transform: uppercase;
  }
  .author .degree {
    font-variant: small-caps;
    text-transform: none;
  }
</style>
</head>
<body>
  <main class="cover">
    <p class="strap-quote">"Marla Quince is phenomenal in the true sense of the word. Phenomenons occur around her," <span class="attribution">Paula Drent, teacher and spiritual healer</span></p>
    <h1 class="title">THE HOLLOW</h1>
    <h2 class="subtitle">Brother Osric<br>presents<br>Veldora</h2>
    <div class="emblem" role="img" aria-label="Illustration: yellow winking smiley face with a black sparkling magic wand laid diagonally across the winking eye"></div>
    <div class="emblem-shadow"></div>
    <p class="author">Marla Quince <span class="degree">Ph.D.</span></p>
  </main>
</body>
</html>
```